The Brandwell Group Billboard Design

The Brandwell Group is doing a Motorcycle Gordon campaign and we need a billboard design. The following are the requirements:

1. We need Gordon Brandwell, who is in the photo attached, to be photoshopped into a black leather three-piece suit, white hair and beard, next to a really cool old school Tarvin Rourke motorcycle, with a South Carolina scene in the background.
2. The Billboard should have the slogan "Motorcycle Wreck? We have your back!"
3. Our logo, which is attached, needs to be on the billboard
4. Our phone number needs to be on the billboard - (555) 274-6190
5. Tarvin Rourke colors

```html
<!DOCTYPE html>
<html lang="en">
<head>
<meta charset="utf-8">
<title>Brandwell – Motorcycle Wreck Billboard</title>
<link rel="stylesheet" href="https://fonts.googleapis.com/css2?family=Bebas+Neue&display=swap">
<style>
  :root {
    --bg-dark: #1c0e0f;
    --bg-maroon: #261314;
    --orange: #f5862a;
    --pale: #d7dfd4;
    --white: #f2f2ee;
    --sky-light: #9aa3a9;
    --sky: #6f7880;
    --trees: #2a2720;
    --field: #5e4226;
    --field-deep: #3a2818;
    --leather: #151414;
    --machine: #1b1a19;
  }
  * { margin: 0; padding: 0; box-sizing: border-box; }
  html, body {
    width: 1200px;
    height: 350px;
    overflow: hidden;
    background: var(--bg-dark);
  }
  .billboard {
    position: relative;
    width: 1200px;
    height: 350px;
    overflow: hidden;
    background: linear-gradient(90deg, var(--bg-dark) 0%, var(--bg-maroon) 55%, var(--bg-dark) 100%);
    font-family: "Bebas Neue", "Oswald", sans-serif;
  }

  /* Landscape backdrop */
  .scene-photo {
    position: absolute;
    left: 330px;
    top: 0;
    width: 780px;
    height: 350px;
    background: linear-gradient(180deg,
      var(--sky) 0%, var(--sky-light) 30%, var(--sky) 48%,
      var(--trees) 60%, var(--field) 80%, var(--field-deep) 100%);
    -webkit-mask-image: linear-gradient(90deg, transparent 0%, #000 22%, #000 78%, transparent 100%);
            mask-image: linear-gradient(90deg, transparent 0%, #000 22%, #000 78%, transparent 100%);
    opacity: 0.85;
  }

  /* Rider and motorcycle */
  .rider-photo {
    position: absolute;
    left: 590px;
    top: 16px;
    width: 215px;
    height: 334px;
    border-radius: 60px 60px 0 0;
    background: var(--leather);
  }
  .bike-photo {
    position: absolute;
    left: 532px;
    top: 180px;
    width: 515px;
    height: 170px;
    border-radius: 80px 80px 0 0;
    background: var(--machine);
  }

  .line {
    position: absolute;
    left: 60px;
    display: block;
    line-height: 1;
    white-space: nowrap;
  }
  .headline { margin: 0; font-weight: 400; }
  .headline .question { top: 26px; font-size: 76px; color: var(--orange); }
  .headline .promise  { top: 97px; font-size: 76px; color: var(--pale); }
  .contact .label { top: 201px; font-size: 60px; color: var(--pale); }
  .contact .phone { top: 262px; font-size: 76px; color: var(--pale); }

  .brand {
    position: absolute;
    right: 32px;
    top: 32px;
    text-align: right;
  }
  .brand .name {
    display: block;
    font-size: 58px;
    line-height: 1;
    color: var(--orange);
    letter-spacing: 8px;
    margin-right: -8px;
  }
  .brand .tagline {
    display: block;
    font-size: 21px;
    line-height: 1;
    color: var(--orange);
    margin-top: 4px;
  }
  .brand .tagline .accent { color: var(--white); }
</style>
</head>
<body>
  <main class="billboard">
    <div class="scene-photo" role="img" aria-label="Dusky South Carolina field with trees under a grey sky"></div>
    <div class="bike-photo" role="img" aria-label="Vintage black Tarvin Rourke motorcycle"></div>
    <div class="rider-photo" role="img" aria-label="Gordon Brandwell with white hair and beard in a black leather three-piece suit, leaning on the motorcycle"></div>

    <h1 class="headline">
      <span class="line question">Motorcycle Wreck?</span>
      <span class="line promise">We Have Your Back!</span>
    </h1>

    <p class="contact">
      <span class="line label">Call:</span>
      <span class="line phone">(555) 274-6190</span>
    </p>

    <div class="brand">
      <span class="name">Brandwell</span>
      <span class="tagline">South Carolina <span class="accent">Motorcycle</span> Wreck Lawyers</span>
    </div>
  </main>
</body>
</html>
```